business card design and letterhead for a building inspection company. We have a pre-purchase building and pest inspection ( i inspect house before people purchase it)
Updates

Tilda has been so so responsive and good, i highly recommend her

Industry/Entity Type

Building

Contact Information for Business Card

audience, solicitor, real estate agent, mortgage brokerthe rest of the info will be in the attachement business card

```html
<!DOCTYPE html>
<html lang="en">
<head>
<meta charset="utf-8">
<title>Soundhome Property Inspections – Business Card</title>
<link href="https://fonts.googleapis.com/css2?family=Open+Sans:wght@400;600;700&display=swap" rel="stylesheet">
<style>
  :root {
    --bg: #9c9c9c;
    --card: #ffffff;
    --blue: #1f7fd0;
    --ink: #2b2b2b;
    --muted: #555b61;
  }
  * { margin: 0; padding: 0; box-sizing: border-box; }
  html, body { width: 1200px; height: 894px; overflow: hidden; }
  body {
    background: var(--bg);
    font-family: "Open Sans", Arial, sans-serif;
    position: relative;
  }
  .card {
    position: absolute;
    width: 540px;
    height: 309px;
    background: var(--card);
    overflow: hidden;
    box-shadow: 0 10px 24px rgba(0,0,0,.25);
  }
  .card-back { left: 620px; top: 110px; }
  .card-front { left: 40px; top: 470px; }
  .edge-band { position: absolute; inset: 0; width: 100%; height: 100%; }

  .brand { position: absolute; }
  .brand-row { display: flex; align-items: center; gap: 10px; }
  .brand-mark { width: 16px; height: 16px; background: var(--blue); }
  .brand-name {
    font-weight: 700; color: var(--blue);
    font-size: 38px; letter-spacing: 1px; line-height: 1;
  }
  .brand-sub {
    color: var(--blue); font-weight: 600; font-size: 14px;
    letter-spacing: 1.5px; margin-left: 26px; margin-top: 2px;
  }
  .brand-tag {
    color: var(--blue); font-size: 12px; letter-spacing: 1px;
    margin-left: 26px;
  }

  .card-back .brand { left: 140px; top: 70px; }
  .socials {
    position: absolute; left: 40px; right: 40px; top: 205px;
    display: flex; justify-content: space-between;
  }
  .social { display: flex; align-items: center; gap: 8px; color: var(--muted); font-size: 13px; }
  .social-dot { width: 14px; height: 14px; background: var(--blue); }
  .back-block { position: absolute; right: 0; top: 200px; width: 18px; height: 38px; background: var(--blue); }

  .front-block { position: absolute; left: 0; top: 62px; width: 30px; height: 48px; background: var(--blue); }
  .card-front .brand { left: 48px; top: 58px; }
  .person { position: absolute; left: 48px; top: 160px; }
  .person-name { font-weight: 700; font-size: 24px; color: var(--ink); letter-spacing: 1px; }
  .person-role { color: var(--blue); font-size: 14px; letter-spacing: 5px; }

  .contacts { position: absolute; left: 300px; top: 200px; list-style: none; }
  .contact { display: flex; align-items: flex-start; gap: 10px; font-size: 12px; font-weight: 600; color: var(--muted); line-height: 1.35; margin-bottom: 6px; }
  .contact svg { width: 16px; height: 16px; flex: none; fill: var(--blue); }
</style>
</head>
<body>

<section class="card card-back">
  <svg class="edge-band" viewBox="0 0 540 309" preserveAspectRatio="none" aria-hidden="true">
    <polygon points="200,0 540,0 540,22" fill="var(--blue)"/>
  </svg>
  <div class="brand">
    <div class="brand-row"><span class="brand-mark"></span><span class="brand-name">SOUNDHOME</span></div>
    <div class="brand-sub">PROPERTY INSPECTIONS</div>
    <div class="brand-tag">the building and pest expert</div>
  </div>
  <div class="socials">
    <span class="social"><span class="social-dot"></span>yourname</span>
    <span class="social"><span class="social-dot"></span>@yourname</span>
    <span class="social"><span class="social-dot"></span>yourname</span>
  </div>
  <div class="back-block"></div>
</section>

<section class="card card-front">
  <svg class="edge-band" viewBox="0 0 540 309" preserveAspectRatio="none" aria-hidden="true">
    <polygon points="220,0 540,0 540,26" fill="var(--blue)"/>
  </svg>
  <div class="front-block"></div>
  <div class="brand">
    <div class="brand-row"><span class="brand-mark"></span><span class="brand-name">SOUNDHOME</span></div>
    <div class="brand-sub">PROPERTY INSPECTIONS</div>
    <div class="brand-tag">the building and pest expert</div>
  </div>
  <div class="person">
    <div class="person-name">SARAH TILDA</div>
    <div class="person-role">GENERAL MANAGER</div>
  </div>
  <ul class="contacts">
    <li class="contact">
      <svg viewBox="0 0 16 16"><path d="M8 1 1 7.5h2V15h4v-4h2v4h4V7.5h2z"/></svg>
      <span>14 Harbour Lane, Level 3<br>Ridgeview</span>
    </li>
    <li class="contact">
      <svg viewBox="0 0 16 16"><path d="M8 1a7 7 0 1 0 0 14A7 7 0 0 0 8 1zm0 1.4c.8.9 1.4 2.3 1.6 4H6.4C6.6 4.7 7.2 3.3 8 2.4zM2.5 7.4h2.6c.1 1.6.4 3 1 4.1a5.6 5.6 0 0 1-3.6-4.1zm0-1a5.6 5.6 0 0 1 3.6-4.1c-.6 1.1-.9 2.5-1 4.1zm3.9 1h3.2c-.1 1.6-.7 3-1.6 4-.9-1-1.5-2.4-1.6-4zm3.5 4.1c.6-1.1.9-2.5 1-4.1h2.6a5.6 5.6 0 0 1-3.6 4.1zm1-5.1c-.1-1.6-.4-3-1-4.1a5.6 5.6 0 0 1 3.6 4.1z"/></svg>
      <span>www.soundhome-inspect.com</span>
    </li>
    <li class="contact">
      <svg viewBox="0 0 16 16"><path d="M1 3h14v10H1zm1.5 1.2L8 8.6l5.5-4.4z"/></svg>
      <span>sarah@soundhome-inspect.com</span>
    </li>
    <li class="contact">
      <svg viewBox="0 0 16 16"><path d="M4 1.5 6.3 4 5 5.8c.8 1.9 2.3 3.4 4.2 4.2L11 8.7l2.5 2.3-1.3 2.8C7 13.5 2.5 9 2.2 3.8z"/></svg>
      <span>013 555 0192</span>
    </li>
  </ul>
</section>

</body>
</html>
```